International Property Consultancy

Brief Overview:

I need a dynamic and well designed website that is easy to use and understand. It has to be unique and different to generic templates that most websites seem to be these days. PLEASE NO GENERIC TEMPLATES FROM THE INTERNET.

Our business has 10 years experience working on struggling international developments that we then work in-house for to turn around and brings bout success. We stay within a project often for long periods of time until success is achieved. We are unique in our approach and completely different to the standard routes to market for many developments. The site is for developers to see what we have done in regards to previous projects, as such we want to incorporate video into this site with a strong design aesthetic. There will be videos of the past projects we have worked on, which will act as case studies.

I like very simple but punchy websites, that people can navigate and understand very easily. Also a big fan of unique and well thought out design aesthetic.

Initial Site layout thoughts:

1) Homepage:
2) About Us
3) What we've done / Work
This part has the projects we have worked on (France, Portugal, London, Morocco). Each one will have some video content and photo images, but also would be good to have a succinct way to mention what we did and the successes in a clever and punchy way.

4) Contact Us

* This is just a guideline. Would be open to input and creative direction on your own part.

*More details and websites we like can be seen in the brief doc attached.

PLEASE VIEW THE WIREFRAME WORD DOC ATTACHED.

Here there are also some more examples to help:

Here are just a few examples of websites and what I like about them:

- www.velmoro.com (clean, nice geometric design aesthetic, good animation when loading and changing pages well thought out all though also coulee be considered a bit dull and basic after the initial homepage slide)
- https://www.farbridgehub.net (Clean site, quite clinical, lacks video content and doesn't engage greatly).
- https://ruskotile.com (minimal, and like how it mixes the design aesthetic more with video and photo content)

- https://www.amberquillworks.com (like the layout of this and how it displays the projects and work section)

- https://brisk.com (Good use of video content)

- https://loomfield.studio (minimal to the point and mixes design with video and animation etc...)

Here is another couple of cool websites that may help give you some direction: https://halvenquay.com www.brisk.com

Hi there, One of the things I thought would be good on the homepage is to add the logo with a 'digital landscape' before flicking down into a slide with video content of the projects... Just an idea but have posted some pics in the brief. We would get this animated for the site. But if you have better ideas, please do run with them. Thanks,

Target Market(s)

Property developers

Number of Pages Required

4 page

Font styles to use
Other font styles liked:
• Read brief

Requirements
Must have
• Needs to be clean, dynamic and easy to follow on desktop and mobile. We will use it as a kind of portfolio website so will need to embed video of past projects we have worked on.

Read brief in docs.
Nice to have
• Clean
Should not have
• Not be another generic template website.
Not have random property stock photos. (We are not a property agency).

```html
<!DOCTYPE html>
<html lang="en">
<head>
<meta charset="utf-8">
<title>Calverant — International Property Consultancy</title>
<link rel="stylesheet" href="https://fonts.googleapis.com/css2?family=Outfit:wght@300;400;500;600;700&display=swap">
<style>
  :root {
    --teal: #134454;
    --ink: #1c1a1b;
    --peach: #f8e1d7;
    --ghost: #ededed;
    --muted: #6b6b6b;
    --line: #bdbdbd;
    --white: #ffffff;
    --fr-blue: #00209f;
    --fr-red: #ed2939;
    --pt-green: #006600;
    --pt-red: #ff0000;
    --ldn-navy: #00005e;
    --ldn-red: #cf142b;
  }
  * { box-sizing: border-box; margin: 0; padding: 0; }
  html, body { width: 1200px; height: 3662px; overflow: hidden; background: var(--white); }
  body { font-family: "Outfit", sans-serif; color: var(--ink); position: relative; }
  .abs { position: absolute; }

  /* header */
  .brand { left: 110px; top: 14px; font-size: 44px; font-weight: 500; letter-spacing: -1px; color: var(--ink); }
  .nav { right: 110px; top: 32px; display: flex; gap: 38px; font-size: 16px; font-weight: 500; }
  .nav a { color: var(--ink); text-decoration: none; }
  .nav a.active { color: var(--teal); border-top: 3px solid var(--teal); padding-top: 4px; margin-top: -7px; }

  /* hero */
  .hero-peach { left: 188px; top: 86px; width: 244px; height: 628px; background: var(--peach); border-radius: 40px; }
  .hero-teal { left: 630px; top: 112px; width: 388px; height: 622px; background: var(--teal); border-radius: 40px 40px 0 0; }
  .hero-edge { right: 0; top: 86px; width: 40px; height: 130px; background: var(--teal); }
  .hero-wordmark { left: 108px; top: 160px; font-size: 176px; font-weight: 500; letter-spacing: -5px; line-height: 1; color: var(--ink); }
  .hero-title { left: 110px; top: 372px; font-size: 56px; font-weight: 500; }
  .hero-sub { left: 111px; top: 458px; width: 540px; font-size: 34px; font-weight: 400; line-height: 54px; }
  .dots { left: 111px; top: 650px; display: flex; gap: 8px; }
  .dots span { width: 37px; height: 5px; background: #d8d8d8; }
  .dots span:first-child { background: var(--teal); }
  .scroll { left: 580px; top: 612px; text-align: center; font-size: 15px; color: var(--muted); }
  .mouse { width: 36px; height: 58px; border: 2px solid #999; border-radius: 18px; margin: 0 auto 10px; position: relative; background: var(--white); }
  .mouse::after { content: ""; position: absolute; left: 16px; top: 12px; width: 2px; height: 10px; background: #999; }

  /* about */
  .ghost-block { background: var(--ghost); border-radius: 60px; }
  .section-title { left: 0; width: 1200px; text-align: center; font-size: 88px; font-weight: 700; letter-spacing: -2px; color: var(--ink); }
  .about-copy { left: 150px; width: 900px; top: 988px; text-align: center; font-size: 20px; font-weight: 300; line-height: 34px; color: #333; }
  .about-copy p + p { margin-top: 32px; }
  .video { left: 345px; top: 1255px; width: 508px; height: 309px; background: linear-gradient(180deg, #4d5161 0%, #a7adb8 35%, #6d7480 60%, #2c3038 100%); box-shadow: 0 4px 14px rgba(0,0,0,.3); overflow: hidden; }
  .video-brand { left: 10px; top: 4px; font-size: 26px; color: var(--white); font-weight: 500; }
  .video-menu { right: 12px; top: 14px; width: 20px; height: 14px; border-top: 2px solid #fff; border-bottom: 2px solid #fff; }
  .video-menu::after { content: ""; position: absolute; left: 0; top: 4px; width: 20px; height: 2px; background: #fff; }
  .video-caption { left: 228px; top: 152px; width: 272px; padding: 6px 8px; background: rgba(19,68,84,.55); color: #fff; font-size: 14px; line-height: 18px; }
  .play { left: 224px; top: 124px; width: 60px; height: 60px; border-radius: 50%; background: rgba(0,0,0,.75); }
  .play::after { content: ""; position: absolute; left: 23px; top: 17px; border-left: 22px solid #fff; border-top: 13px solid transparent; border-bottom: 13px solid transparent; }

  /* work */
  .work-bg { left: 592px; top: 1647px; width: 422px; height: 620px; background: linear-gradient(180deg, #d9cfcd 0%, #cbb7ad 60%, #e2d4cc 100%); border-radius: 0 0 60px 60px; }
  .work-photo { left: 192px; top: 1674px; width: 312px; height: 618px; background: radial-gradient(circle at 40% 25%, #9bc8d8 0%, #1e6aa0 40%, #0b3a66 100%); border-radius: 120px 120px 0 0; }
  .work-edge { left: 0; top: 1647px; width: 24px; height: 90px; background: #0e4a88; }
  .card { top: 1837px; height: 371px; overflow: hidden; box-shadow: 0 2px 6px rgba(0,0,0,.15); }
  .card-label { left: 0; width: 100%; bottom: 42px; text-align: center; color: #fff; font-size: 44px; font-weight: 600; }
  .card-fr { left: 111px; width: 355px; background: linear-gradient(90deg, var(--fr-blue) 48%, var(--fr-red) 48%); }
  .card-pt { left: 520px; width: 355px; background: linear-gradient(90deg, var(--pt-green) 36%, var(--pt-red) 36%); }
  .card-ldn { left: 928px; width: 272px; background: var(--ldn-navy); }
  .card-ldn .v { left: 163px; top: 0; width: 28px; height: 100%; background: var(--ldn-red); }
  .card-ldn .h { left: 0; top: 173px; width: 100%; height: 28px; background: var(--ldn-red); }
  .card-ldn .card-label { text-align: left; padding-left: 82px; }
  .arrow { left: 218px; top: 176px; }

  /* contact */
  .field { font-size: 19px; font-weight: 300; color: #555; border-bottom: 1px solid var(--line); padding-bottom: 14px; }
  .submit { left: 530px; top: 2801px; width: 140px; height: 58px; background: var(--teal); color: #fff; font-size: 20px; font-weight: 600; display: flex; align-items: center; justify-content: center; }

  /* info */
  .info-peach { left: 188px; top: 2972px; width: 318px; height: 430px; background: var(--peach); border-radius: 40px; }
  .info-title { left: 110px; top: 3038px; font-size: 28px; font-weight: 500; }
  .info-item { left: 110px; display: flex; align-items: center; gap: 42px; font-size: 21px; font-weight: 400; line-height: 32px; }
  .icon { width: 58px; height: 58px; border: 1.5px solid #999; border-radius: 50%; display: flex; align-items: center; justify-content: center; background: var(--white); flex-shrink: 0; }
  .info-photo { left: 630px; top: 3000px; width: 388px; height: 421px; background: linear-gradient(160deg, #bfe3f7 0%, #3d8fd0 40%, #174e86 75%, #0e2f55 100%); border-radius: 190px 190px 0 0; }

  /* footer */
  .socials { left: 527px; top: 3476px; display: flex; gap: 10px; }
  .socials span { width: 42px; height: 42px; border: 1.5px solid #999; border-radius: 50%; }
  .footer-brand { left: 0; width: 1200px; top: 3522px; text-align: center; font-size: 58px; font-weight: 500; letter-spacing: -1px; }
  .copyright { left: 0; width: 1200px; top: 3592px; text-align: center; font-size: 16px; color: var(--muted); }
</style>
</head>
<body>

<header>
  <div class="abs brand">calverant.</div>
  <nav class="abs nav">
    <a class="active" href="#home">HOME</a>
    <a href="#about">ABOUT US</a>
    <a href="#work">WORK</a>
    <a href="#contact">CONTACT US</a>
  </nav>
</header>

<section id="home">
  <div class="abs hero-peach"></div>
  <div class="abs hero-teal"></div>
  <div class="abs hero-edge"></div>
  <div class="abs hero-wordmark">calverant.</div>
  <h1 class="abs hero-title">We are Calverant</h1>
  <p class="abs hero-sub">We fulfill international property developments</p>
  <div class="abs dots"><span></span><span></span><span></span></div>
  <div class="abs scroll"><div class="mouse"></div>Scroll</div>
</section>

<section id="about">
  <div class="abs ghost-block" style="left:298px;top:800px;width:600px;height:460px;"></div>
  <h2 class="abs section-title" style="top:868px;">ABOUT US</h2>
  <div class="abs about-copy">
    <p>We fulfil international property developments in a truly unique way. We've worked on projects around the world taking developments from fields to award winning resorts, and tired underachieving developments to overachieving goliaths.</p>
    <p>By creating a unique and bespoke in-house white-label strategy that allows each project to be the only beneficiary of the work we do.</p>
  </div>
  <div class="abs video" role="img" aria-label="Project video still of a city skyline">
    <div class="abs video-brand">calverant.</div>
    <div class="abs video-menu"></div>
    <div class="abs play"></div>
    <div class="abs video-caption">A proven consultancy specialising in the fulfilment of international property developments</div>
  </div>
</section>

<section id="work">
  <div class="abs work-bg" role="img" aria-label="Soft-focus background photograph"></div>
  <div class="abs work-photo" role="img" aria-label="Photograph of glowing fibre optic strands"></div>
  <div class="abs work-edge"></div>
  <h2 class="abs section-title" style="top:1700px;">WORK</h2>
  <div class="abs card card-fr"><div class="abs card-label">FRANCE</div></div>
  <div class="abs card card-pt"><div class="abs card-label">PORTUGAL</div></div>
  <div class="abs card card-ldn">
    <div class="abs v"></div><div class="abs h"></div>
    <svg class="abs arrow" width="40" height="20" viewBox="0 0 40 20"><path d="M2 10h32M26 3l8 7-8 7" stroke="#fff" stroke-width="3" fill="none"/></svg>
    <div class="abs card-label">LONDON</div>
  </div>
</section>

<section id="contact">
  <div class="abs ghost-block" style="left:298px;top:2378px;width:600px;height:460px;"></div>
  <h2 class="abs section-title" style="top:2406px;">CONTACT US</h2>
  <div class="abs field" style="left:230px;top:2542px;width:356px;">Your Name</div>
  <div class="abs field" style="left:630px;top:2542px;width:357px;">Your Email</div>
  <div class="abs field" style="left:230px;top:2627px;width:356px;">Your Phone no</div>
  <div class="abs field" style="left:630px;top:2627px;width:357px;">Your Company</div>
  <div class="abs field" style="left:230px;top:2708px;width:757px;">Tell us about your project</div>
  <div class="abs submit">SUBMIT</div>
</section>

<section id="info">
  <div class="abs info-peach"></div>
  <div class="abs info-photo" role="img" aria-label="Photograph looking up at glass skyscrapers"></div>
  <h3 class="abs info-title">Contact Information</h3>
  <div class="abs info-item" style="top:3107px;">
    <span class="icon"><svg width="16" height="22" viewBox="0 0 16 22"><path d="M8 1a7 7 0 0 0-7 7c0 5 7 13 7 13s7-8 7-13a7 7 0 0 0-7-7z" fill="#134454"/><circle cx="8" cy="8" r="2.6" fill="#fff"/></svg></span>
    <span>12 Marlow Lane<br>London EC2A 4QT</span>
  </div>
  <div class="abs info-item" style="top:3197px;">
    <span class="icon"><svg width="22" height="16" viewBox="0 0 22 16"><rect width="22" height="16" rx="2" fill="#134454"/><path d="M1 2l10 7 10-7" stroke="#fff" stroke-width="1.6" fill="none"/></svg></span>
    <span>hello@calverant.com</span>
  </div>
  <div class="abs info-item" style="top:3279px;">
    <span class="icon"><svg width="20" height="20" viewBox="0 0 20 20"><path d="M4 1l4 4-2.5 2.5a12 12 0 0 0 7 7L15 12l4 4-3 3C8 19 1 12 1 4z" fill="#134454"/></svg></span>
    <span>+44 (0)00 0000 0000</span>
  </div>
</section>

<footer>
  <div class="abs socials"><span></span><span></span><span></span></div>
  <div class="abs footer-brand">calverant.</div>
  <div class="abs copyright">© 2020 Calverant. All rights reserved. Privacy &nbsp;|&nbsp; Terms of use</div>
</footer>

</body>
</html>
```